Dorvanski Law Rebrand

I am recreating my law firm website. I got a new logo and would like to recreate the website to match the new logo. the website is dorvanskilaw.com

```html
<!DOCTYPE html>
<html lang="en">
<head>
<meta charset="utf-8">
<title>Dorvanski Law, PLLC</title>
<link href="https://fonts.googleapis.com/css2?family=Abril+Fatface&family=Montserrat:wght@400;500;600;700&display=swap" rel="stylesheet">
<style>
:root{
  --blue:#0b4a8b;
  --topbar:#8c99ad;
  --ink:#1a1a1a;
  --text:#555a60;
  --card:#f2f2f4;
  --dark:#1f1f22;
  --white:#ffffff;
  --hero-light:#f1efec;
  --hero-warm:#d8bd9c;
}
*{margin:0;padding:0;box-sizing:border-box}
html,body{width:1200px;height:3304px;overflow:hidden}
body{position:relative;background:var(--white);font-family:'Montserrat',sans-serif;color:var(--text)}
.display{font-family:'Abril Fatface',serif;color:var(--ink);font-weight:400}
.btn{position:absolute;display:flex;align-items:center;justify-content:center;background:var(--blue);color:var(--white);font-size:12.5px;font-weight:600}

/* top bar */
.topbar{position:absolute;left:0;top:0;width:1200px;height:36px;background:var(--topbar);color:var(--white);font-size:12.5px}
.topbar .item{position:absolute;top:0;height:36px;display:flex;align-items:center;gap:7px}
.topbar .divider{position:absolute;left:772px;top:8px;width:1px;height:20px;background:rgba(255,255,255,.7)}

/* header */
.header{position:absolute;left:0;top:36px;width:1200px;height:90px;background:var(--white)}
.brand{position:absolute;left:75px;top:30px;display:flex;align-items:center;gap:8px;font-size:19px;font-weight:700;letter-spacing:2px;color:var(--blue)}
.brand .mark{width:14px;height:14px;background:var(--blue)}
.nav a{position:absolute;top:38px;font-size:12.5px;color:#555;text-decoration:none}

/* hero */
.hero-edge{position:absolute;left:0;top:126px;width:1200px;height:710px;background:var(--blue);clip-path:polygon(0 0,100% 0,100% 614px,50% 710px,0 614px)}
.hero-photo{position:absolute;left:0;top:126px;width:1200px;height:700px;background:linear-gradient(90deg,var(--hero-light) 0%,var(--hero-light) 50%,var(--hero-warm) 100%);clip-path:polygon(0 0,100% 0,100% 612px,50% 700px,0 612px)}
.hero-content{position:absolute;left:0;top:126px;width:1200px;height:700px}
.hero-content h1{position:absolute;left:75px;top:142px;font-size:51px;line-height:56px}
.hero-content p{position:absolute;left:75px;width:530px;font-size:12.5px;line-height:19px;color:#4a4a4a}
.scroll-cue{position:absolute;left:582px;top:609px}

/* welcome */
.portrait{position:absolute;left:125px;top:950px;width:474px;height:434px;background:linear-gradient(135deg,#3b3b3d,#5e5e60 55%,#2c2c2e)}
.welcome h2{position:absolute;left:648px;top:960px;font-size:44px;line-height:45px}
.welcome p{position:absolute;left:648px;width:430px;font-size:12.5px;line-height:19px}

/* practice */
.section-title{position:absolute;left:0;width:1200px;text-align:center;font-size:44px;line-height:48px}
.pcard{position:absolute;width:331px;height:246px;background:var(--card);text-align:center}
.pcard .icon{position:absolute;left:126px;top:15px;width:78px;height:78px;border-radius:50%;background:var(--blue);display:flex;align-items:center;justify-content:center}
.pcard h3{position:absolute;left:0;top:104px;width:100%;font-size:19px}
.pcard p{position:absolute;left:33px;top:134px;width:265px;font-size:11.5px;line-height:18.6px}
.practice-photo{position:absolute;left:435px;top:1576px;width:330px;height:503px;background:linear-gradient(180deg,#d9d5cf 0%,#9d9891 50%,#b89a78 100%)}

/* blog */
.bcard{position:absolute;top:2318px;width:328px;height:327px;background:var(--card)}
.bcard .thumb{height:250px}
.bcard h3{position:absolute;left:30px;top:265px;font-size:19px}
.bcard a{position:absolute;left:30px;top:296px;font-size:12px;font-weight:500;color:var(--blue);text-decoration:underline}

/* footer */
.footer-edge{position:absolute;left:0;top:2754px;width:1200px;height:550px;background:var(--blue);clip-path:polygon(0 102px,50% 0,100% 102px,100% 100%,0 100%)}
.footer{position:absolute;left:0;top:2754px;width:1200px;height:550px;background:var(--dark);clip-path:polygon(0 105px,50% 8px,100% 105px,100% 100%,0 100%);color:var(--white)}
.footer-brand{position:absolute;left:0;top:138px;width:1200px;display:flex;justify-content:center;align-items:center;gap:10px;font-size:27px;font-weight:700;letter-spacing:4px}
.footer-brand .mark{width:18px;height:18px;background:var(--white)}
.fcol{position:absolute;top:280px}
.fcol h4{font-family:'Abril Fatface',serif;font-weight:400;font-size:22px;margin-bottom:10px}
.fcol li{list-style:none;font-size:12.5px;line-height:22.5px}
.contact-row{display:flex;gap:10px;font-size:12.5px;line-height:16.5px;margin-bottom:10px}
.contact-row svg{margin-top:3px;flex:none}
.newsletter p{font-size:12.5px;margin-bottom:15px}
.signup{display:flex;width:354px;height:36px}
.signup span{flex:1;background:var(--white);color:#777;font-size:10.5px;padding-left:18px;display:flex;align-items:center}
.signup b{width:43px;background:var(--blue);display:flex;align-items:center;justify-content:center}
.footer-rule{position:absolute;left:75px;top:501px;width:1050px;height:1px;background:#55575c}
.copyright{position:absolute;left:0;top:519px;width:1200px;text-align:center;font-size:12px}
</style>
</head>
<body>

<div class="topbar">
  <div class="item" style="left:75px">
    <svg width="13" height="13" viewBox="0 0 16 16"><circle cx="8" cy="8" r="7.5" fill="#fff"/><path d="M8 4v4.5l3 1.5" stroke="#8c99ad" stroke-width="1.6" fill="none"/></svg>
    Mon - Fri&nbsp; 8AM - 5PM
  </div>
  <div class="item" style="left:621px">
    <svg width="13" height="13" viewBox="0 0 16 16"><path d="M3 1l3 .5 1 3.5-2 1.5a9 9 0 0 0 4.5 4.5l1.5-2 3.5 1 .5 3-2 1.5C6.5 14.5 1.5 9.5 1.5 3z" fill="#fff"/></svg>
    (555) 410-2763
  </div>
  <div class="divider"></div>
  <div class="item" style="left:818px">
    <svg width="11" height="14" viewBox="0 0 12 16"><path d="M6 0a6 6 0 0 1 6 6c0 4-6 10-6 10S0 10 0 6a6 6 0 0 1 6-6z" fill="#fff"/><circle cx="6" cy="6" r="2.2" fill="#8c99ad"/></svg>
    240 E. Marlow Avenue Suite B Brenton, Texas 77410
  </div>
</div>

<header class="header">
  <div class="brand"><span class="mark"></span>DORVANSKI LAW</div>
  <nav class="nav">
    <a style="left:542px">Home</a>
    <a style="left:621px">Practices Areas</a>
    <a style="left:755px">About Me</a>
    <a style="left:857px">Blog</a>
  </nav>
  <div class="btn" style="left:914px;top:28px;width:210px;height:35px">Schedule a Consultation</div>
</header>

<section class="hero">
  <div class="hero-edge"></div>
  <div class="hero-photo" role="img" aria-label="Photo of a bronze Lady Justice statue and a wooden gavel in a bright office"></div>
  <div class="hero-content">
    <h1 class="display">Personal Legal<br>Solutions in Life's Most<br>Difficult Moments</h1>
    <p style="top:320px">Helping clients navigate probate, guardianships, estate planning, &amp; other civil disputes by providing personal attention to each client; knowing their objectives; understanding their needs; and then thinking creatively to achieve those goals.</p>
    <p style="top:388px">Every case is different and each client is unique - I believe that when an attorney approaches them as such, the outcomes can be better than ever anticipated.</p>
    <div class="btn" style="left:75px;top:443px;width:211px;height:34px">Schedule a Consultation</div>
    <svg class="scroll-cue" width="36" height="60" viewBox="0 0 36 60"><rect x="1" y="1" width="34" height="58" rx="17" fill="none" stroke="#fff" stroke-width="1.5"/><path d="M18 20v20M12 34l6 6 6-6" stroke="#fff" stroke-width="1.5" fill="none"/></svg>
  </div>
</section>

<section class="welcome">
  <div class="portrait" role="img" aria-label="Portrait photo of the attorney in a navy suit"></div>
  <h2 class="display">Welcome To<br>Dorvanski Law, PLLC</h2>
  <p style="top:1069px">It is my honor to provide quality legal services at a reasonable price to clients that I enjoy working with and for. I am grateful for all my clients and the trust they place in me to represent them.</p>
  <p style="top:1138px">My practice focuses on Probate, Adult Guardianships, and Trust Administration and Litigation. I also represent clients in other general civil litigation matters.&nbsp; Finally, I handle estate planning for families of modest means.</p>
  <p style="top:1226px">As your attorney, I would educate you about the law as it pertains to your situation, guide you through your options, and then help you to achieve your desired objectives from those options.</p>
  <p style="top:1295px">Schedule your consultation today.</p>
  <div class="btn" style="left:648px;top:1331px;width:119px;height:35px">Read More</div>
</section>

<section class="practice">
  <h2 class="display section-title" style="top:1488px">Practice Area</h2>

  <div class="pcard" style="left:94px;top:1576px">
    <div class="icon"><svg width="34" height="38" viewBox="0 0 34 38" fill="none" stroke="#fff" stroke-width="1.6"><rect x="6" y="2" width="22" height="32" rx="2"/><path d="M11 10h12M11 16h12M11 22h7"/><path d="M20 30v-5M24 30v-8"/></svg></div>
    <h3 class="display">Probate and Trusts</h3>
    <p>Guiding clients through the legal process of administering a deceased person's estate, ensuring that assets are distributed according to their wishes while addressing any legal complexities that may arise.</p>
  </div>

  <div class="practice-photo" role="img" aria-label="Photo of an attorney reading a law book at a desk in front of bookshelves"></div>

  <div class="pcard" style="left:775px;top:1576px">
    <div class="icon"><svg width="38" height="36" viewBox="0 0 38 36" fill="none" stroke="#fff" stroke-width="1.6"><rect x="3" y="4" width="32" height="26" rx="2"/><circle cx="12" cy="20" r="5"/><path d="M21 12h9M21 17h9M22 26v-4M26 26v-6M30 26v-8"/></svg></div>
    <h3 class="display">Estate Planning</h3>
    <p>Helping individuals and families create tailored plans that safeguard their assets, ensure their wishes are fulfilled, and provide for their loved ones after they pass away.</p>
  </div>

  <div class="pcard" style="left:94px;top:1833px">
    <div class="icon"><svg width="36" height="36" viewBox="0 0 36 36" fill="none" stroke="#fff" stroke-width="1.6"><path d="M18 3l12 5v9c0 8-6 13-12 16C12 30 6 25 6 17V8z"/><circle cx="18" cy="15" r="4"/><path d="M11 26c2-4 12-4 14 0"/></svg></div>
    <h3 class="display">Adult Guardianships</h3>
    <p>Assisting families in securing legal guardianship for individuals who are unable to make decisions for themselves, ensuring that their rights and well-being are protected through compassionate...</p>
  </div>

  <div class="pcard" style="left:775px;top:1833px">
    <div class="icon"><svg width="36" height="36" viewBox="0 0 36 36" fill="none" stroke="#fff" stroke-width="1.6"><rect x="7" y="3" width="22" height="28"/><path d="M11 8h4v4h-4zM21 8h4v4h-4zM11 16h4v4h-4zM21 16h4v4h-4zM3 33h30"/></svg></div>
    <h3 class="display">Civil Litigation</h3>
    <p>Representing clients in legal disputes, advocating for their rights and interests in various matters such as contract disputes, personal injury claims, and property issues, with a focus on achieving...</p>
  </div>

  <div class="btn" style="left:494px;top:2103px;width:212px;height:35px">Schedule a Consultation</div>
</section>

<section class="blog">
  <h2 class="display section-title" style="top:2241px">Our Blog</h2>
  <article class="bcard" style="left:90px">
    <div class="thumb" role="img" aria-label="Photo of two colleagues reviewing documents at a table" style="background:linear-gradient(180deg,#55605a,#2e2f31)"></div>
    <h3 class="display">Trusts vs. Wills</h3>
    <a>Read More</a>
  </article>
  <article class="bcard" style="left:435px">
    <div class="thumb" role="img" aria-label="Photo of a lawyer signing papers at a desk" style="background:linear-gradient(180deg,#e2e0dc,#8d8b88)"></div>
    <h3 class="display">Why probate is needed</h3>
    <a>Read More</a>
  </article>
  <article class="bcard" style="left:780px">
    <div class="thumb" role="img" aria-label="Photo of an attorney handing a document to a client" style="background:linear-gradient(180deg,#7a6552,#2f2c2b)"></div>
    <h3 class="display">Estate Planning Essentials</h3>
    <a>Read More</a>
  </article>
</section>

<div class="footer-edge"></div>
<footer class="footer">
  <div class="footer-brand"><span class="mark"></span>DORVANSKI LAW</div>

  <div class="fcol" style="left:132px">
    <h4>Main Links</h4>
    <ul><li>Home</li><li>About Us</li><li>Practice Area</li><li>Blog</li><li>Contact</li></ul>
  </div>

  <div class="fcol" style="left:404px">
    <h4>Contact Us</h4>
    <div class="contact-row"><svg width="13" height="13" viewBox="0 0 16 16"><path d="M3 1l3 .5 1 3.5-2 1.5a9 9 0 0 0 4.5 4.5l1.5-2 3.5 1 .5 3-2 1.5C6.5 14.5 1.5 9.5 1.5 3z" fill="#fff"/></svg><div>Phone<br>(555) 410-2763</div></div>
    <div class="contact-row"><svg width="13" height="13" viewBox="0 0 16 16"><circle cx="8" cy="8" r="7.5" fill="#fff"/><path d="M8 4v4.5l3 1.5" stroke="#1f1f22" stroke-width="1.6" fill="none"/></svg><div>Timing Hour<br>Mon - Fri&nbsp; 8AM - 5PM</div></div>
    <div class="contact-row"><svg width="12" height="15" viewBox="0 0 12 16"><path d="M6 0a6 6 0 0 1 6 6c0 4-6 10-6 10S0 10 0 6a6 6 0 0 1 6-6z" fill="#fff"/><circle cx="6" cy="6" r="2.2" fill="#1f1f22"/></svg><div>Address<br>240 E. Marlow Avenue Suite B<br>Brenton, Texas 77410</div></div>
  </div>

  <div class="fcol newsletter" style="left:711px">
    <h4>Newsletter Sign Up</h4>
    <p>We Will Notify You Of Any Important News</p>
    <div class="signup"><span>Enter Your Email Address...</span><b><svg width="14" height="14" viewBox="0 0 16 16"><path d="M1 7l14-6-5 14-2-6z" fill="#fff"/></svg></b></div>
  </div>

  <div class="footer-rule"></div>
  <div class="copyright">© 2025 Dorvanski Law, PLLC | All Rights Reserved</div>
</footer>

</body>
</html>
```